Product Labels for soaps lines

I have bar soap, liquid soap, lip balm, lotion bar, lotion and bath bomb ,I already have a logo and I need product labels for shape of Square, Circle, Rectangle and oval,

The design need to match my logo.

example of the texts:( rectangle)

Hair Shampoo

100% handmade - Sulfate Free

Ingredients: Canola Oil ,Ricinus Communis (Castor) Seed Oil ,Cocos Nucifera (Coconut) Oil ,Simmondsia Chinensis (Jojoba) Seed Oil ,Aqua ( Water),Potassium hydroxide ,Fragrance

NT WT 8 OZ

Rectangle label measurement : 2 *4 for liquid shampoo
rectangle-horizontal or oval : 2.5*2 for bar soap
Circle : 1.5 for lip balm and 2 ' for lotion bar
rectangle label : 2*3 for lotion
circle label: 2.3 for body butter
rectangle label :1*1.5 facial serum

example of the texts:( medium rectangle)

Natural Body Soap

Ricinus Communis (Castor) Seed Oil ,Cocos Nucifera (Coconut) Oil ,Hydrogenated Palm Oil ,Prunus Amygdalus Dulcis (Sweet Almond) Oil ,Butyrospermum Parkii (Shea Butter) Fruit ,Beeswax ,Oryza Sativa (Rice) Bran Oil ,Olea Europaea (Olive) Oil ,Aqua ( Water),Sodium hydroxide ,Raw Goat Milk,Mica,Fragrance
Approx. 5 OZ

hand Wash/Body Wash lable size 2*4
Ricinus Communis (Castor) Seed Oil ,Cocos Nucifera (Coconut) Oil ,Theobroma Cacao (Cocoa) Seed Butter ,Olea Europaea (Olive) Oil ,Oryza Sativa (Rice) Bran Oil ,Aqua ( Water),Potassium hydroxide ,Fragrance

Avacado Facial Wash lable size 2*4
Canola Oil ,Ricinus Communis (Castor) Seed Oil ,Cocos Nucifera (Coconut) Oil ,Persea Gratissima (Avocado) Oil ,Prunus Amygdalus Dulcis (Sweet Almond) Oil ,Oryza Sativa (Rice) Bran Oil ,Aqua ( Water),Potassium hydroxide ,Fragrance

Lotion Bar
Cocos Nucifera (Coconut) Oil ,Mangifera Indica (Mango) Seed Butter ,Butyrospermum Parkii (Shea Butter) Fruit ,Beewax

Body Butter
Cocos Nucifera (Coconut) Oil ,Butyrospermum Parkii (Shea Butter) Fruit ,Theobroma Cacao (Cocoa) Seed Butter ,Helianthus Annuus (Sunflower) Seed Oil

lip balm,
Olea Europaea (Olive) Oil ,Butyrospermum Parkii (Shea Butter) Fruit ,Vitis Vinifera (Grape) Seed Oil ,Beewax,Fragrance

facial serum:1*1.5
Prunus Armeniaca (Apricot) Kernel Oil ,Argania Spinosa (Argan) Nut Oil ,Simmondsia Chinensis (Jojoba) Seed Oil ,Rosa Canina Fruit Oil

Target Market(s)

Logo color can be changed to a little darker blue

Industry/Entity Type

Hair

Font styles to use
Serif

Colors
fece3e
f04a50
33b7a4
8869ae

Requirements
Must have

• company name " Soap brambleton " is inspired by Tobin of the Saltmarsh, fun and adventurous spirit, design need to be fun ..
Nice to have
• Fun, Simple and eye catching ..

```html
<!DOCTYPE html>
<html lang="en">
<head>
<meta charset="utf-8">
<title>Soap Brambleton – Product Labels</title>
<link rel="stylesheet" href="https://fonts.googleapis.com/css2?family=Cherry+Swash:wght@700&family=Kurale&display=swap">
<style>
  :root {
    --purple: #5b1862;
    --cream: #dedfa3;
    --white: #ffffff;
    --name-ink: #f3f1d2;
    --teal-title: #138a8f;
    --brown: #4a1a12;
    --bubble-light: #fbfbef;
    --bubble-dark: #d3d08f;
    --shadow: #7a7a7a;
  }
  * { box-sizing: border-box; margin: 0; padding: 0; }
  html, body { width: 1200px; height: 1000px; overflow: hidden; background: var(--white); }
  .sheet { position: relative; width: 1200px; height: 1000px; }

  .caption {
    position: absolute;
    font: 18px/1 Arial, Helvetica, sans-serif;
    color: #111;
    transform: translateX(-50%);
    white-space: nowrap;
  }

  .label {
    position: absolute;
    width: 235px;
    background: var(--white);
    border: 1px solid #333;
    overflow: hidden;
  }
  .label__top { position: absolute; left: 0; top: 0; width: 100%; background: var(--purple); }
  .label__band { position: absolute; left: 0; width: 100%; background: var(--cream); }
  .bubbles {
    position: absolute;
    background: radial-gradient(ellipse at 50% 35%, var(--bubble-light) 0%, #ecebc6 55%, var(--bubble-dark) 100%);
    border-radius: 40px 40px 6px 6px;
  }
  .bubbles--round { border-radius: 50%; }

  .brand-name {
    position: absolute; left: 0; width: 100%;
    text-align: center;
    font-family: "Kurale", serif;
    font-weight: 400;
    color: var(--name-ink);
    line-height: 1;
    white-space: nowrap;
  }

  .product-name {
    position: absolute; left: 0; width: 100%;
    text-align: center;
    font-family: "Cherry Swash", serif;
    font-weight: 700;
    color: var(--teal-title);
    line-height: 1;
    white-space: nowrap;
  }
  .claim, .ingredients, .weight {
    position: absolute;
    font-family: "Kurale", serif;
    color: var(--brown);
    white-space: nowrap;
  }
  .claim { left: 0; width: 100%; text-align: center; line-height: 1; }
  .ingredients { line-height: 21px; }

  .round-label { position: absolute; width: 250px; height: 250px; }
</style>
</head>
<body>
<main class="sheet">

  <!-- Liquid shampoo -->
  <p class="caption" style="left:248px; top:51px;">Liquid Shampoo</p>
  <section class="label" style="left:131px; top:107px; height:472px;">
    <div class="label__top" style="height:165px;"></div>
    <p class="brand-name" style="top:70px; font-size:27px;">Soap Brambleton</p>
    <div class="bubbles" role="img" aria-label="Cluster of cream soap bubbles" style="left:4px; top:125px; width:226px; height:45px;"></div>
    <div class="label__band" style="top:165px; height:82px;"></div>
    <h2 class="product-name" style="top:180px; font-size:22px;">Hair Shampoo</h2>
    <p class="claim" style="top:216px; font-size:14px;">100% handmade - Sulfate Free</p>
    <p class="ingredients" style="left:18px; top:256px; font-size:13px;">Ingredients:<br>Coconut Oil, Castor Oil,<br>Jojoba Oil, Sweet Almond Oil,<br>Distilled Water, Potassium<br>hydroxide, Essential Oil</p>
    <p class="weight" style="left:18px; top:382px; font-size:13px;">NT WT 8 oz</p>
    <div class="bubbles bubbles--round" role="img" aria-label="Large soap bubbles" style="left:172px; top:350px; width:58px; height:58px;"></div>
    <div class="bubbles" role="img" aria-label="Cluster of cream soap bubbles" style="left:4px; top:420px; width:226px; height:52px;"></div>
  </section>

  <!-- Bar soap -->
  <p class="caption" style="left:590px; top:146px;">Bar Soap</p>
  <section class="label" style="left:470px; top:205px; height:295px;">
    <div class="label__top" style="height:145px;"></div>
    <p class="brand-name" style="top:54px; font-size:25px;">Soap Brambleton</p>
    <div class="bubbles" role="img" aria-label="Cluster of cream soap bubbles" style="left:18px; top:105px; width:212px; height:42px;"></div>
    <div class="label__band" style="top:145px; height:65px;"></div>
    <h2 class="product-name" style="top:158px; font-size:20px;">Natural Body Soap</h2>
    <p class="claim" style="top:187px; font-size:12px;">100% handmade - Sulfate Free</p>
    <p class="ingredients" style="left:48px; top:224px; font-size:11px; line-height:15px;">Ingredients:<br>Shea Butter &amp; Chamomile</p>
    <p class="weight" style="left:92px; top:272px; font-size:11px;">Approx. 5 oz</p>
    <div class="bubbles" role="img" aria-label="Small soap bubbles" style="left:4px; top:252px; width:78px; height:43px;"></div>
    <div class="bubbles" role="img" aria-label="Small soap bubbles" style="left:196px; top:244px; width:36px; height:51px;"></div>
  </section>

  <!-- Lotion -->
  <p class="caption" style="left:938px; top:145px;">Lotion</p>
  <section class="label" style="left:828px; top:206px; height:353px;">
    <div class="label__top" style="height:165px;"></div>
    <p class="brand-name" style="top:68px; font-size:27px;">Soap Brambleton</p>
    <div class="bubbles" role="img" aria-label="Cluster of cream soap bubbles" style="left:4px; top:122px; width:226px; height:45px;"></div>
    <div class="label__band" style="top:165px; height:82px;"></div>
    <h2 class="product-name" style="top:184px; font-size:22px;">Body Lotion</h2>
    <p class="claim" style="top:220px; font-size:14px;">100% handmade - Sulfate Free</p>
    <p class="ingredients" style="left:22px; top:250px; font-size:13px;">Ingredients:<br>&nbsp;&nbsp;&nbsp;Ingredients, Ingredients,<br>Ingredients, Ingredients etc.</p>
    <p class="weight" style="left:68px; top:323px; font-size:13px;">NT WT ? oz</p>
    <div class="bubbles" role="img" aria-label="Small soap bubbles" style="left:8px; top:322px; width:48px; height:28px;"></div>
    <div class="bubbles" role="img" aria-label="Small soap bubbles" style="left:168px; top:318px; width:62px; height:32px;"></div>
  </section>

  <!-- Lip balm -->
  <p class="caption" style="left:434px; top:635px;">Lip Balm</p>
  <svg class="round-label" style="left:315px; top:682px;" viewBox="0 0 250 250" aria-label="Lip balm round label">
    <defs>
      <clipPath id="lip-clip"><circle cx="125" cy="123" r="117"/></clipPath>
      <linearGradient id="bubble-fill" x1="0" y1="0" x2="0" y2="1">
        <stop offset="0" stop-color="#fbfbef"/><stop offset="1" stop-color="#d3d08f"/>
      </linearGradient>
      <path id="lip-arc" d="M 22 128 A 103 103 0 0 0 228 128"/>
    </defs>
    <circle cx="129" cy="127" r="117" fill="var(--shadow)"/>
    <g clip-path="url(#lip-clip)">
      <rect x="0" y="0" width="250" height="250" fill="var(--cream)"/>
      <rect x="0" y="0" width="250" height="128" fill="var(--purple)"/>
      <rect x="30" y="100" width="188" height="36" rx="18" fill="url(#bubble-fill)" role="img" aria-label="Cluster of cream soap bubbles"/>
    </g>
    <text x="125" y="72" text-anchor="middle" font-family="Kurale, serif" font-size="24" fill="var(--name-ink)">Soap Brambleton</text>
    <text x="120" y="164" text-anchor="middle" font-family="Cherry Swash, serif" font-weight="700" font-size="19" fill="var(--teal-title)">Lip Balm</text>
    <text x="142" y="181" text-anchor="middle" font-family="Kurale, serif" font-size="11" fill="var(--brown)">100%</text>
    <text x="142" y="194" text-anchor="middle" font-family="Kurale, serif" font-size="11" fill="var(--brown)">handmade</text>
    <text font-family="Kurale, serif" font-size="10.5" fill="var(--brown)"><textPath href="#lip-arc">Ingredients: Ingredients: Ingredients: Ingredients: Ingredients:</textPath></text>
  </svg>

  <!-- Lotion bar -->
  <p class="caption" style="left:747px; top:639px;">Lotion Bar</p>
  <svg class="round-label" style="left:620px; top:685px;" viewBox="0 0 250 250" aria-label="Lotion bar round label">
    <defs>
      <clipPath id="bar-clip"><circle cx="125" cy="123" r="117"/></clipPath>
      <path id="bar-arc" d="M 22 128 A 103 103 0 0 0 228 128"/>
    </defs>
    <circle cx="129" cy="127" r="117" fill="var(--shadow)"/>
    <g clip-path="url(#bar-clip)">
      <rect x="0" y="0" width="250" height="250" fill="var(--cream)"/>
      <rect x="0" y="0" width="250" height="128" fill="var(--purple)"/>
      <rect x="30" y="100" width="188" height="36" rx="18" fill="url(#bubble-fill)" role="img" aria-label="Cluster of cream soap bubbles"/>
    </g>
    <text x="125" y="72" text-anchor="middle" font-family="Kurale, serif" font-size="24" fill="var(--name-ink)">Soap Brambleton</text>
    <text x="122" y="164" text-anchor="middle" font-family="Cherry Swash, serif" font-weight="700" font-size="19" fill="var(--teal-title)">Lotion Bar</text>
    <text x="142" y="181" text-anchor="middle" font-family="Kurale, serif" font-size="11" fill="var(--brown)">100%</text>
    <text x="142" y="194" text-anchor="middle" font-family="Kurale, serif" font-size="11" fill="var(--brown)">handmade</text>
    <text font-family="Kurale, serif" font-size="10.5" fill="var(--brown)"><textPath href="#bar-arc">Ingredients: Ingredients: Ingredients: Ingredients: Ingredients:</textPath></text>
  </svg>

</main>
</body>
</html>
```